Yacht Charter Broker needs a magazine page design

We are a travel agent for yachts called Velmoria Yacht Charters. www.velmoriacharters.example We are advertising in a magazine at the grand pacer equine fair - https://plgequinefair.example/ - and need a high-end luxury feeling magazine page.

Target Market(s)

Vacation goers looking to charter a crewed yacht.

Industry/Entity Type

Travel Agent

Requirements
Must have
• luxury feel. logo. website and social media icons if you feel necessary. Our motto is: Inhale. Exhale. Sail.
• Catamaran picture, snorkeling and other island, water looking pictures.
Nice to have
• Open to your design.
Should not have
• Nothing comes to mind.

```html
<!DOCTYPE html>
<html lang="en">
<head>
<meta charset="utf-8">
<title>Velmoria Yacht Charters – Magazine Page Concepts</title>
<link rel="stylesheet" href="https://fonts.googleapis.com/css2?family=Montserrat:wght@300;400;500;800&display=swap">
<style>
  :root {
    --board: #c4c4c4;
    --ink: #161616;
    --white: #ffffff;
    --paper: #f4f4f4;
    --navy: #1b2a4a;
    --deep: #0a1b24;
    --sea-dark: #0f4a73;
    --sea-mid: #1a6a98;
    --sea-light: #2fa3c9;
    --rock: #8c8a82;
    --rock-light: #b3afa5;
  }
  * { box-sizing: border-box; margin: 0; padding: 0; }
  html, body { width: 924px; height: 1200px; overflow: hidden; }
  body {
    background: var(--board);
    font-family: "Montserrat", Arial, sans-serif;
    color: var(--ink);
    position: relative;
  }
  .sample-label {
    position: absolute;
    font-size: 17px;
    font-weight: 500;
  }
  .page {
    position: absolute;
    width: 365px;
    height: 471px;
    overflow: hidden;
    box-shadow: 0 3px 8px rgba(0,0,0,.35);
  }
  .photo { position: absolute; inset: 0; }
  .photo--cove {
    background: linear-gradient(180deg, var(--rock-light) 0%, var(--rock) 45%, var(--sea-light) 58%, var(--sea-mid) 100%);
  }
  .photo--cove-dark {
    background: linear-gradient(180deg, var(--rock-light) 0%, var(--rock) 45%, var(--sea-light) 56%, var(--sea-mid) 78%, var(--deep) 100%);
  }
  .photo--aerial {
    background: linear-gradient(200deg, var(--sea-dark) 0%, var(--sea-mid) 45%, var(--sea-light) 75%, var(--sea-dark) 100%);
  }
  .headline { position: absolute; color: var(--white); line-height: .9; white-space: nowrap; }
  .headline .light { font-weight: 300; display: block; }
  .headline .bold { font-weight: 800; display: block; letter-spacing: -3px; }
  .vertical { writing-mode: vertical-rl; transform: rotate(180deg); }

  .brand { position: absolute; }
  .brand__name { font-size: 20px; font-weight: 400; letter-spacing: 4px; line-height: 1; }
  .brand__tag { font-size: 5px; letter-spacing: 1.6px; text-align: right; margin-top: 3px; text-transform: uppercase; }
  .brand__web { font-size: 7.5px; letter-spacing: 2.4px; margin-top: 9px; }
  .brand--dark { color: var(--navy); }
  .brand--light { color: var(--white); }

  .social { position: absolute; display: flex; gap: 6px; }
  .social span { width: 14px; height: 14px; border-radius: 50%; border: 1.2px solid currentColor; }
  .social--dark { color: var(--navy); }
  .social--light { color: var(--white); }
  .social--small span { width: 12px; height: 12px; }

  .footer-band { position: absolute; left: 0; right: 0; bottom: 0; }
  .footer-band--paper { height: 80px; background: var(--paper); }
  .footer-band--deep { height: 90px; background: var(--deep); }

  .motto-frame {
    position: absolute; left: 80px; top: -2px; width: 206px; height: 193px;
    border: 1.5px solid var(--white); border-top: none;
  }
  .caption {
    position: absolute; left: 0; right: 0; top: 1117px;
    text-align: center; font-size: 27px; font-weight: 400;
  }
</style>
</head>
<body>

  <div class="sample-label" style="left:61px;top:36px;">Sample 1</div>
  <div class="sample-label" style="left:491px;top:36px;">Sample 2</div>
  <div class="sample-label" style="left:61px;top:567px;">Sample 3</div>
  <div class="sample-label" style="left:491px;top:567px;">Sample 4</div>

  <!-- Concept 1 -->
  <section class="page" style="left:61px;top:71px;">
    <div class="photo photo--cove" role="img" aria-label="Sailing yacht anchored in turquoise water beneath tall limestone cliffs"></div>
    <div class="headline" style="left:146px;top:219px;">
      <span class="light" style="font-size:44px;">INHALE,</span>
      <span class="light" style="font-size:44px;">EXHALE,</span>
      <span class="bold" style="font-size:82px;margin-top:-2px;">SAIL</span>
    </div>
    <div class="footer-band footer-band--paper"></div>
    <div class="brand brand--dark" style="left:23px;top:410px;">
      <div class="brand__name">VELMORIA</div>
      <div class="brand__tag">Yacht Charter Broker</div>
      <div class="brand__web">www.velmoriacharters.example</div>
    </div>
    <div class="social social--dark" style="left:257px;top:436px;"><span></span><span></span><span></span><span></span></div>
  </section>

  <!-- Concept 2 -->
  <section class="page" style="left:491px;top:71px;">
    <div class="photo photo--cove-dark" role="img" aria-label="Sailing yacht anchored in a cliff-lined turquoise cove"></div>
    <div class="headline vertical" style="left:10px;top:10px;height:248px;font-size:60px;font-weight:300;text-align:start;">INHALE</div>
    <div class="headline" style="left:82px;top:6px;font-size:58px;font-weight:300;">EXHALE</div>
    <div class="headline vertical" style="left:222px;top:14px;height:340px;font-size:150px;font-weight:800;letter-spacing:-6px;line-height:.88;">SAIL</div>
    <div class="brand brand--light" style="left:23px;top:412px;">
      <div class="brand__name">VELMORIA</div>
      <div class="brand__tag">Yacht Charter Broker</div>
      <div class="brand__web">www.velmoriacharters.example</div>
    </div>
    <div class="social social--light social--small" style="left:274px;top:440px;"><span></span><span></span><span></span><span></span></div>
  </section>

  <!-- Concept 3 -->
  <section class="page" style="left:61px;top:603px;">
    <div class="photo photo--aerial" role="img" aria-label="Aerial view of a white catamaran on deep blue and turquoise sea"></div>
    <div class="brand brand--light" style="left:23px;top:20px;">
      <div class="brand__name">VELMORIA</div>
      <div class="brand__tag">Yacht Charter Broker</div>
      <div class="brand__web">www.velmoriacharters.example</div>
    </div>
    <div class="headline vertical" style="left:104px;top:240px;height:215px;font-size:46px;font-weight:300;line-height:1.02;">INHALE,<br>EXHALE,</div>
    <div class="headline vertical" style="left:196px;top:0;height:468px;font-size:206px;font-weight:800;letter-spacing:-8px;line-height:.82;">SAIL</div>
    <div class="social social--light social--small" style="left:22px;top:445px;"><span></span><span></span><span></span><span></span></div>
  </section>

  <!-- Concept 4 -->
  <section class="page" style="left:491px;top:603px;">
    <div class="photo photo--aerial" role="img" aria-label="Aerial view of a white catamaran on open blue water"></div>
    <div class="motto-frame"></div>
    <div class="headline" style="left:98px;top:34px;">
      <span class="light" style="font-size:45px;">INHALE</span>
      <span class="light" style="font-size:45px;">EXHALE</span>
      <span class="bold" style="font-size:80px;margin-left:-5px;">SAIL</span>
    </div>
    <div class="footer-band footer-band--deep"></div>
    <div class="brand brand--light" style="left:23px;top:405px;">
      <div class="brand__name">VELMORIA</div>
      <div class="brand__tag">Yacht Charter Broker</div>
      <div class="brand__web">www.velmoriacharters.example</div>
    </div>
    <div class="social social--light social--small" style="left:274px;top:432px;"><span></span><span></span><span></span><span></span></div>
  </section>

  <div class="caption">Yacht Charter Broker needs a magazine page design</div>

</body>
</html>
```